Preschool Website

Looking to have a one page splash with a contact us form that uses some kind of verification to keep bots from filling out the form. We would like for it to be dynamic for both mobile and desktop. Would like to have it show up in search engines for preschool in are area. Would like to include a link to the website are current parents use for payment information.

Target Market(s)

Young Adults with Childrens

Industry/Entity Type

Preschool

Coding

Coded - Design and coding required

Number of Pages Required

1 page

Colors

Designer to choose colors to be used in the design.

Requirements
Must have
• Searchable in Vextra
• Contact us form
• Name
• Phone
• Email
• Message box
• Form must have code entered to submit to prevent junk emails
• Link to the website we use for parents to make payments
• our phone and address clickable on device to make call or map on phone
Should not have
• more then one page

```html
<!DOCTYPE html>
<html lang="en">
<head>
<meta charset="utf-8">
<title>Brightsteps Preschool – Communication is key</title>
<link href="https://fonts.googleapis.com/css2?family=Baloo+2:wght@700;800&family=Poppins:wght@400;500;600&display=swap" rel="stylesheet">
<style>
:root{
  --green:#16d68e;
  --magenta:#cd11a1;
  --panel:#d6d6d6;
  --white:#ffffff;
  --text-light:#f4f4f4;
  --photo-top:#6a6a68;
  --photo-bottom:#4d453c;
  --illus-pink:#f2c4e6;
  --illus-deep:#c3148f;
}
*{box-sizing:border-box;margin:0;padding:0}
html,body{width:958px;height:1200px;overflow:hidden;background:var(--white)}
body{position:relative;font-family:'Poppins',sans-serif}
.page{position:relative;width:958px;height:1200px;overflow:hidden}
.bar{position:absolute;left:0;width:958px;background:var(--green)}
.bar--top{top:0;height:5px;z-index:3}
.bar--bottom{top:1194px;height:6px}

.hero{position:absolute;top:0;left:0;width:958px;height:567px;overflow:hidden}
.hero__photo{position:absolute;inset:0;
  background:linear-gradient(180deg,var(--photo-top) 0%,#625f5a 55%,var(--photo-bottom) 100%)}
.brand-name{position:absolute;left:79px;top:24px;font-family:'Baloo 2',sans-serif;font-weight:800;
  font-size:30px;line-height:1;color:var(--green);text-decoration:none}

.contact-form{position:absolute;left:79px;top:89px;width:282px;height:458px;
  background:var(--panel);border-radius:8px;box-shadow:0 2px 6px rgba(0,0,0,.25);z-index:2}
.field{position:absolute;left:20px;width:240px;height:32px;border:none;border-radius:8px;
  background:var(--white);box-shadow:0 2px 3px rgba(0,0,0,.3);
  font-family:'Poppins',sans-serif;font-size:14px;color:var(--green);padding:0 29px;outline:none}
.field::placeholder{color:var(--green)}
.field--name{top:27px}
.field--phone{top:83px}
.field--email{top:138px}
.field--code{top:194px}
.field--message{top:250px;height:128px;padding-top:6px;resize:none}
.btn-contact{position:absolute;left:148px;top:401px;width:112px;height:35px;border:none;
  border-radius:8px;background:var(--magenta);color:var(--white);
  font-family:'Poppins',sans-serif;font-weight:500;font-size:14px}

.stripes{position:absolute;left:0;top:0;z-index:1}

.hero__copy{position:absolute;left:500px;top:214px;width:380px;z-index:2}
.hero__title{font-family:'Baloo 2',sans-serif;font-weight:800;font-size:33px;line-height:1.1;color:var(--green);white-space:nowrap}
.hero__text{margin-top:4px;font-size:13.6px;line-height:20px;color:var(--text-light)}

.section-title{position:absolute;font-family:'Baloo 2',sans-serif;font-weight:800;font-size:32px;
  color:var(--magenta);text-align:center;width:340px}
.title--touch{left:70px;top:658px}
.title--pay{left:548px;top:654px}

.illus{position:absolute;border-radius:40%;
  background:radial-gradient(circle at 55% 45%,var(--illus-deep) 0%,#df5fbf 45%,var(--illus-pink) 75%,rgba(255,255,255,0) 100%)}
.illus--phone{left:172px;top:730px;width:135px;height:140px}
.illus--map{left:174px;top:970px;width:129px;height:111px;border-radius:12px}
.illus--payment{left:637px;top:822px;width:163px;height:160px;border-radius:46%;
  background:radial-gradient(circle at 55% 55%,var(--illus-deep) 0%,#e06ec4 35%,var(--illus-pink) 60%,var(--illus-pink) 100%)}

.btn{position:absolute;display:flex;align-items:center;justify-content:center;width:223px;height:48px;
  border-radius:9px;background:var(--magenta);color:var(--white);text-decoration:none;
  font-weight:600;font-size:14px}
.btn--number{left:128px;top:896px}
.btn--address{left:128px;top:1096px}
.btn--payment{left:607px;top:1004px}
</style>
</head>
<body>
<div class="page">
  <div class="bar bar--top"></div>

  <header class="hero">
    <div class="hero__photo" role="img" aria-label="Blurred classroom desk with stacked books, coloured pencils and ABC wooden blocks"></div>
    <a class="brand-name" href="#">Brightsteps</a>

    <svg class="stripes" width="958" height="567" viewBox="0 0 958 567">
      <line x1="531" y1="420" x2="370" y2="590" stroke="var(--magenta)" stroke-width="16" stroke-linecap="round"/>
      <line x1="420" y1="468" x2="300" y2="590" stroke="var(--green)" stroke-width="20" stroke-linecap="round"/>
    </svg>

    <form class="contact-form">
      <input class="field field--name" type="text" placeholder="Your Name">
      <input class="field field--phone" type="tel" placeholder="Your Phone">
      <input class="field field--email" type="email" placeholder="Your Email">
      <input class="field field--code" type="text" placeholder="Enter Your Code">
      <textarea class="field field--message" placeholder="Your Message"></textarea>
      <button class="btn-contact" type="submit">Contact Us</button>
    </form>

    <div class="hero__copy">
      <h1 class="hero__title">Communication is key</h1>
      <p class="hero__text">Lorem ipsum dolor sit amet, consectetur adipisicing elit, sed do eiusmod tempor incididunt ut labore et dolore magna aliqua. Ut enim ad minim veniam, quis nostrud exercitation ullamco laboris nisi ut aliquip.</p>
    </div>
  </header>

  <h2 class="section-title title--touch">Get In Touch</h2>
  <div class="illus illus--phone" role="img" aria-label="Illustration of a hand holding a smartphone with contact cards"></div>
  <a class="btn btn--number" href="tel:">Get Our Number</a>
  <div class="illus illus--map" role="img" aria-label="Illustration of a folded map with a location pin"></div>
  <a class="btn btn--address" href="#">Get Our Addres</a>

  <h2 class="section-title title--pay">Get to Payment</h2>
  <div class="illus illus--payment" role="img" aria-label="Illustration of a hand paying with a card at a payment terminal"></div>
  <a class="btn btn--payment" href="#">Make Your Payment</a>

  <div class="bar bar--bottom"></div>
</div>
</body>
</html>
```